A4 Single Page Brochure for Private Cloud Offerings

Theme: Futuristic Tech Company

Brightholm Systems is looking to offer private cloud services for our enterprise customers in Perth-based data-centres that provides our clients with a lower-cost alternative to Nimbra or QKS yielding better performance.

We are looking for a single A4 brochure with a great graphics design theme to promote these services.

We will be providing five tiers:
- Starter
- Growth
- Professional
- Premier
- Elite

Each plan must list on the brochure the Max VMs, CPU cores, Memory and SSD storage allocated. Refer to the uploaded PNG file.

The brochure must list the following selling points:

- Hosted in a local Perth-based TIER3 and TIER4 datacentres
- WA owned hosting - support local
- Low latency - ultra fast local hosting
- Includes Orvane Host Datacentre licensing
- Includes Valdrex Managed Firewalls for Enterprise level threat detection
- Includes all infrastructure maintenance services
- Full self management of VMs through customer portal
- Includes a 1gbps Internet link
- Predictable fixed monthly fee with no dynamic billing
- No additional charges for Storage Transactions, Internet Usage, VM Snapshots, Datacentre Bandwidth Usage and Firewall Traffic Usage.
- Highly available cluster, no single point of failure.
- Pricing is based on 36 months commit
- Yearly rate increases capped to a maximum of Australian CPI
- All plans have 24/7/365 support with dedicated after hours number.
- Managed backup and managed disaster recovery services can be added to plans

Service provided in accordance with our terms and conditions.

We need the ability to EDIT the brochure to adjust pricing after we receive the final project.

I have uploaded more details on these plans under the attachment PrivateCloudPlans.png.

Please do not utilise "Pushing the Boundaries of Technology" - our brand is being replaced with "Specialised Consulting". New website is under development but not launched yet.

Target Market(s)

Information Technology Sector

Colors
0054AA
0677BA
7BADD7
CADEEF
E8F1F8

Requirements
Must have
• Theme of Brightholm is Blue
Should not have
• Extremely stock imagary that just looks "cheap and stock"

```html
<!DOCTYPE html>
<html lang="en">
<head>
<meta charset="utf-8">
<title>Brightholm Systems – Private Cloud Services</title>
<link href="https://fonts.googleapis.com/css2?family=Krona+One&family=Poppins:wght@400;500;600;700&display=swap" rel="stylesheet">
<style>
:root{
  --navy:#1b2a8c;
  --royal:#0054aa;
  --bright:#1177d8;
  --sky:#7badd7;
  --pale:#cadeef;
  --mist:#e8f1f8;
  --ink:#222;
  --grey-bg:#efefef;
  --wedge:#b3b3b3;
  --cell-a:#d9d9d9;
  --cell-b:#cdcdcd;
}
*{margin:0;padding:0;box-sizing:border-box}
html,body{width:1200px;height:1200px;overflow:hidden;background:var(--grey-bg)}
body{font-family:'Poppins',sans-serif;color:var(--ink);position:relative}
.page{position:absolute;left:186px;top:15px;width:1253px;height:1773px;background:#fff;transform:scale(.66);transform-origin:0 0;overflow:hidden}
.abs{position:absolute}
.brand{left:72px;top:92px;display:flex;align-items:center;gap:16px;font-weight:700;font-size:40px;color:var(--navy);letter-spacing:1px}
.brand-mark{width:40px;height:40px;background:var(--royal)}
.hero-art{left:0;top:0;width:1253px;height:870px}
.title{left:70px;top:248px;font-family:'Krona One',sans-serif;color:#fff;font-size:64px;line-height:67px;letter-spacing:-1px}
.subtitle{left:107px;top:470px;color:#fff;font-weight:600;font-size:26px;line-height:32px}
.subtitle-rule{left:76px;top:472px;width:3px;height:62px;background:#fff}
.intro{left:72px;top:612px;width:1010px;font-size:22px;line-height:28px}
.tiers-kicker{left:68px;top:736px;font-weight:700;font-size:18px;color:#111}
.tiers-head{left:66px;top:754px;font-weight:700;font-size:36px;color:var(--bright)}
.labels{left:67px;top:808px;width:300px;height:282px;border-radius:26px 0 0 26px;background:linear-gradient(90deg,#1a2a90,#2446b8);overflow:hidden}
.labels div{height:50px;display:flex;align-items:center;padding-left:28px;color:#fff;font-size:20px}
.labels .hl{background:linear-gradient(90deg,#1e6fd6,#2f86e8)}
.labels .cost{height:82px;font-weight:700;font-size:20px}
.base{left:300px;top:1040px;width:882px;height:50px;background:var(--navy);border-radius:0 0 26px 0}
.col{top:740px;width:174px;height:340px;border-radius:22px;overflow:hidden;background:var(--cell-a);box-shadow:-4px 0 8px rgba(0,0,0,.12)}
.col .head{height:68px;display:flex;align-items:center;justify-content:center;color:#fff;font-weight:700;font-size:19px}
.col .cell{height:50px;display:flex;align-items:center;justify-content:center;font-size:20px;color:#222}
.col .cell:first-of-type{height:58px}
.col .cell.alt{background:var(--cell-b)}
.price{position:absolute;left:23px;bottom:0;width:128px;height:60px;border-radius:22px 22px 0 0;background:var(--bright);color:#fff;font-weight:700;font-size:20px;display:flex;align-items:center;justify-content:center}
.pointer{top:1090px;width:0;height:0;border-left:24px solid transparent;border-right:24px solid transparent;border-top:22px solid var(--royal)}
.offer-box{left:74px;top:1158px;width:1105px;height:472px;border:2px solid #9a9a9a;border-radius:30px}
.offer-title{left:456px;top:1134px;padding:0 20px;background:#fff;font-size:37px;color:#111}
.offer-title b{color:var(--bright);font-weight:700}
.offer-list{list-style:none;display:flex;flex-direction:column;font-size:19px;line-height:21px;color:#222}
.offer-list li{position:relative;padding-left:24px}
.offer-list li::before{content:"";position:absolute;left:0;top:4px;width:13px;height:13px;border-radius:50%;background:var(--navy)}
.offer-list li::after{content:"";position:absolute;left:4px;top:6px;width:3px;height:6px;border:solid #fff;border-width:0 2px 2px 0;transform:rotate(45deg)}
.terms{left:188px;top:1577px;width:878px;height:53px;border-radius:26px 26px 0 0;background:var(--pale);display:flex;align-items:center;justify-content:center;font-size:22px;color:#333}
.contact{left:74px;top:1668px;width:1110px;display:flex;align-items:center;font-size:24px;color:#222}
.contact .call{font-weight:700;font-size:27px;color:var(--navy);margin-right:30px}
.contact .item{display:flex;align-items:center;gap:12px;margin-right:30px}
.contact .item:last-child{margin-right:0}
.icon{width:32px;height:32px;border-radius:50%;background:var(--navy);display:flex;align-items:center;justify-content:center}
</style>
</head>
<body>
<div class="page">
  <svg class="abs hero-art" viewBox="0 0 1253 870">
    <defs>
      <linearGradient id="bandFill" x1="0" y1="0" x2="0.6" y2="1">
        <stop offset="0" stop-color="#1f63c9"/>
        <stop offset="1" stop-color="#1b2590"/>
      </linearGradient>
      <linearGradient id="photoFill" x1="0" y1="0" x2="1" y2="1">
        <stop offset="0" stop-color="#b88a6a"/>
        <stop offset=".45" stop-color="#3c5f95"/>
        <stop offset="1" stop-color="#1d2b44"/>
      </linearGradient>
    </defs>
    <polygon points="1253,320 1253,862 1101,600" fill="var(--wedge)"/>
    <polygon points="0,195 636,195 582,290 745,587 0,587" fill="url(#bandFill)"/>
    <polygon points="766,0 1089,0 1251,290 1089,587 766,587 606,290" fill="var(--royal)"/>
    <polygon points="772,25 1077,25 1226,290 1077,558 772,558 633,290" fill="#fff"/>
    <polygon points="781,35 1069,35 1213,290 1069,549 781,549 646,290" fill="url(#photoFill)" role="img" aria-label="Photo of a hand using a stylus on a tablet with a glowing cloud computing graphic"/>
  </svg>

  <div class="abs brand"><span class="brand-mark"></span>Brightholm Systems</div>

  <h1 class="abs title">PRIVATE<br>CLOUD<br>SERVICES</h1>
  <div class="abs subtitle-rule"></div>
  <p class="abs subtitle">For our enterprise customers in<br>Perth-based data-centres</p>

  <p class="abs intro">Brightholm Systems is looking to offer private cloud services for our enterprise customers in Perth-based data-centres that provides our clients with a lower-cost alternative to Nimbra or QKS yielding better performance.</p>

  <div class="abs tiers-kicker">WE WILL BE PROVIDING</div>
  <div class="abs tiers-head">FIVE TIERS</div>

  <div class="abs labels">
    <div style="height:58px">Max VMs</div>
    <div>CPU cores</div>
    <div class="hl">Memory (GB)</div>
    <div>Storage SSD (TB)</div>
    <div class="cost">MONTHLY COST</div>
  </div>
  <div class="abs base"></div>

  <div class="abs col" style="left:310px"><div class="head" style="background:#7c7c7c">STARTER</div><div class="cell">5</div><div class="cell alt">8</div><div class="cell">64</div><div class="cell alt">3</div><div class="price">$1,028.01</div></div>
  <div class="abs col" style="left:484px"><div class="head" style="background:#575757">GROWTH</div><div class="cell">10</div><div class="cell alt">16</div><div class="cell">128</div><div class="cell alt">8</div><div class="price">$3,426.64</div></div>
  <div class="abs col" style="left:658px"><div class="head" style="background:#8a8a8a">PROFESSIONAL</div><div class="cell">15</div><div class="cell alt">32</div><div class="cell">192</div><div class="cell alt">15</div><div class="price">$4,626.05</div></div>
  <div class="abs col" style="left:833px"><div class="head" style="background:#575757">PREMIER</div><div class="cell">20</div><div class="cell alt">48</div><div class="cell">256</div><div class="cell alt">20</div><div class="price">$5,482.72</div></div>
  <div class="abs col" style="left:1008px"><div class="head" style="background:#8a8a8a">ELITE</div><div class="cell">25</div><div class="cell alt">64</div><div class="cell">320</div><div class="cell alt">30</div><div class="price">$7,196.07</div></div>

  <div class="abs pointer" style="left:373px"></div>
  <div class="abs pointer" style="left:547px"></div>
  <div class="abs pointer" style="left:721px"></div>
  <div class="abs pointer" style="left:896px"></div>
  <div class="abs pointer" style="left:1071px"></div>

  <div class="abs offer-box"></div>
  <h2 class="abs offer-title" style="font-weight:400">WHAT <b>WE OFFER</b></h2>

  <ul class="abs offer-list" style="left:108px;top:1203px;width:330px;gap:26px">
    <li>Hosted in a local Perth-based TIER3 and TIER4 datacentres</li>
    <li>WA owned hosting - support local</li>
    <li>Low latency - ultra fast local hosting</li>
    <li>Includes Orvane Host Datacentre licensing</li>
    <li>Includes Valdrex Managed Firewalls for Enterprise level threat detection</li>
  </ul>
  <ul class="abs offer-list" style="left:477px;top:1203px;width:320px;gap:21px">
    <li>Includes all infrastructure maintenance services</li>
    <li>Full self management of VMs through customer portal</li>
    <li>Includes a 1gbps Internet link</li>
    <li>Predictable fixed monthly fee with no dynamic billing</li>
    <li>No additional charges for Storage Transactions, Internet Usage, VM Snapshots, Datacentre Bandwidth Usage and Firewall Traffic Usage.</li>
  </ul>
  <ul class="abs offer-list" style="left:831px;top:1203px;width:330px;gap:21px">
    <li>Highly available cluster, no single point of failure.</li>
    <li>Pricing is based on 36 months commit</li>
    <li>Yearly rate increases capped to a maximum of Australian CPI</li>
    <li>All plans have 24/7/365 support with dedicated after hours number.</li>
    <li>Managed backup and managed disaster recovery services can be added to plans</li>
  </ul>

  <div class="abs terms">service provided in accordance with our terms and conditions</div>

  <div class="abs contact">
    <span class="call">CALL US NOW</span>
    <span class="item"><span class="icon"><svg width="18" height="18" viewBox="0 0 24 24"><path fill="#fff" d="M6.6 10.8a15.1 15.1 0 0 0 6.6 6.6l2.2-2.2a1 1 0 0 1 1-.25 11.4 11.4 0 0 0 3.6.57 1 1 0 0 1 1 1V20a1 1 0 0 1-1 1A17 17 0 0 1 3 4a1 1 0 0 1 1-1h3.5a1 1 0 0 1 1 1c0 1.25.2 2.45.57 3.57a1 1 0 0 1-.25 1z"/></svg></span>021.555.0147</span>
    <span class="item"><span class="icon"><svg width="18" height="18" viewBox="0 0 24 24"><rect x="3" y="6" width="18" height="12" rx="1.5" fill="none" stroke="#fff" stroke-width="2"/><path d="M3 7l9 6 9-6" fill="none" stroke="#fff" stroke-width="2"/></svg></span>info@brightholm.com</span>
    <span class="item"><span class="icon"><svg width="18" height="18" viewBox="0 0 24 24" fill="none" stroke="#fff" stroke-width="1.8"><circle cx="12" cy="12" r="9"/><ellipse cx="12" cy="12" rx="4" ry="9"/><path d="M3 12h18M5 7h14M5 17h14"/></svg></span>www.brightholm.com</span>
  </div>
</div>
</body>
</html>
```